UK young peoples' debating organisation needs flyers for tournament + promotion for major club laun

I need a flyer for the tournament but also sell the after-school clubs on offer.

Needs to be modern, energetic and fun, challenging the traditional idea of debating as simply academic and elitist.

Must appeal to busy headteachers as well as parents and children.

Target Market(s)

Headteachers; children aged 8 - 11 and their parents

Industry/Entity Type

Education

Font styles to use
Serif
Decorative

Colors

Designer to choose colors to be used in the design.

Requirements
Must have
• The Vantor Oratory logo, plus the Brindlecombe Town Council Logo. The text attached on word doc. (writing in brackets and italics are directions, not to be included as text).
• A space theme (rockets? Stars?/ relates to Vantor. Ideas of movement, aspiration, aiming high etc.
Nice to have
Should not have
• anything relating to pure academia and tradition (mortar boards, suits and ties etc); mo

```html
<!DOCTYPE html>
<html lang="en">
<head>
<meta charset="utf-8">
<title>Vantor Oratory – Tournament and Club Flyers</title>
<link href="https://fonts.googleapis.com/css2?family=Fjalla+One&family=Love+Ya+Like+A+Sister&family=Open+Sans:wght@400;600;700&family=Patrick+Hand&display=swap" rel="stylesheet">
<style>
:root{
  --bg:#3b3b3b;
  --red:#d3141c;
  --red-dark:#b3121a;
  --orange:#f36f10;
  --orange-light:#ffb000;
  --yellow:#ffd21f;
  --blue:#1947c9;
  --blue-dark:#0f2f9e;
  --green:#2e9b1e;
  --green-light:#5cc22a;
  --pink:#e8245f;
  --white:#ffffff;
}
*{box-sizing:border-box;margin:0;padding:0}
html,body{width:1200px;height:1200px;overflow:hidden}
body{background:var(--bg);position:relative;font-family:"Open Sans",sans-serif}
.page{position:absolute;width:683px;height:960px;transform:scale(.8);transform-origin:0 0;overflow:hidden;background:var(--white);box-shadow:0 6px 18px rgba(0,0,0,.45)}
.page--tournament{left:34px;top:263px}
.page--clubs{left:614px;top:263px}
.abs{position:absolute}

/* ---------- Tournament page ---------- */
.hero-photo{left:0;top:0;width:472px;height:270px;background:linear-gradient(160deg,#f2f2f2 0%,#cfcfcf 45%,#8a6f66 80%,#5a4a48 100%)}
.brand-tag{left:360px;top:48px;font-family:"Fjalla One",sans-serif;font-size:20px;color:var(--red);line-height:1.05;text-align:center;width:100px}
.orange-field{left:0;top:270px;width:683px;height:690px;background:radial-gradient(circle at 45% 22%,#ffe11f 0%,var(--orange-light) 30%,var(--orange) 65%,#ea4f12 100%)}
.edge-strip{left:665px;top:0;width:18px;height:270px;background:var(--white)}
.ribbon{left:472px;top:0;width:193px;height:420px;background:var(--red);clip-path:polygon(0 0,100% 0,100% 66%,50% 100%,0 66%)}
.ribbon-chevron{left:465px;top:285px;width:207px;height:130px;background:var(--red-dark);clip-path:polygon(0 0,50% 60%,100% 0,100% 22%,50% 92%,0 22%)}
.seal{left:492px;top:12px;width:150px;height:150px;border-radius:50%;background:var(--white);border:6px solid var(--blue);display:flex;align-items:center;justify-content:center;text-align:center;font-weight:700;font-size:14px;color:var(--blue);padding:14px;line-height:1.25}
.ribbon-text{left:478px;top:178px;width:182px;text-align:center;color:var(--white);font-size:13px;line-height:1.3}
.invite-banner{left:0;top:309px;width:378px;height:68px;background:var(--blue);color:var(--white);font-family:"Patrick Hand",cursive;font-weight:400;font-size:18px;line-height:20px;text-align:center;padding:4px 8px 0 14px;border-top:3px solid #5a86ff}
.board-paper{left:28px;top:428px;width:344px;height:262px;background:var(--white);transform:rotate(-1deg)}
.board-post{top:650px;width:8px;height:75px;background:#5b3418}
.board{left:40px;top:441px;width:333px;height:220px;background:linear-gradient(160deg,var(--green-light),var(--green) 60%,#23801a);color:var(--white);padding:12px 10px 0 8px;font-size:11px;line-height:15px}
.board li{list-style:none;position:relative;padding-left:17px;margin-bottom:10px}
.board li::before{content:"✲";position:absolute;left:0;top:0;font-size:12px}
.board .em{font-size:13.5px}
.kids-photo{left:402px;top:432px;width:281px;height:470px;background:linear-gradient(170deg,#f7b98f 0%,#e98a5a 30%,#e6789f 60%,#3b5fb8 100%);clip-path:polygon(25% 0,60% 8%,100% 0,100% 100%,0 100%,0 25%)}
.blue-band{left:0;top:700px;width:683px;height:260px;background:linear-gradient(180deg,#2a5be0,var(--blue-dark));clip-path:polygon(0 22px,100% 0,100% 100%,0 100%)}
.launch-copy{left:32px;top:743px;width:360px;color:var(--white);font-family:"Fjalla One",sans-serif;font-size:13.5px;line-height:19px}
.launch-copy p{margin-bottom:10px}
.launch-copy .hot{color:var(--red)}
.support{left:32px;top:875px;width:360px;color:var(--yellow);font-family:"Fjalla One",sans-serif;font-size:18px;line-height:24px}
.red-foot{left:0;top:896px;width:683px;height:64px;background:var(--red);clip-path:polygon(0 38px,100% 0,100% 100%,0 100%)}
.foot-web{left:480px;top:922px;color:var(--white);font-family:"Fjalla One",sans-serif;font-size:14px;display:flex;align-items:center;gap:8px}

/* ---------- Clubs page ---------- */
.sun-band{left:0;top:0;width:683px;height:150px;background:var(--yellow)}
.colour-band{left:0;top:0;width:683px;height:150px;background:linear-gradient(90deg,#e8603a,#c25a9a 35%,#4a78c9 65%,#4fae5a);clip-path:polygon(0 98px,683px 8px,683px 42px,0 138px)}
.orange-stripe{left:0;top:0;width:683px;height:160px;background:var(--orange);clip-path:polygon(0 138px,683px 42px,683px 70px,0 152px)}
.white-cut{left:0;top:0;width:683px;height:170px;background:var(--white);clip-path:polygon(0 152px,683px 70px,683px 170px,0 170px)}
.tagline{left:128px;top:152px;width:520px;text-align:center;font-family:"Love Ya Like A Sister",cursive;font-weight:400;color:var(--pink);font-size:36px;line-height:36px}
.call-banner{left:178px;top:246px;width:505px;height:70px;background:var(--red);color:var(--yellow);font-family:"Fjalla One",sans-serif;font-weight:400;font-size:29px;display:flex;align-items:center;padding-left:12px;white-space:nowrap}
.call-arrows{left:78px;top:246px}
.group-photo{left:20px;top:330px;width:405px;height:232px;background:linear-gradient(180deg,#fbe7d8 0%,#f0b38a 35%,#e2484a 70%,#4a78c9 100%)}
.blue-field{left:0;top:440px;width:683px;height:520px;background:linear-gradient(180deg,#2450da,var(--blue) 50%,var(--blue-dark));clip-path:polygon(0 140px,683px 0,683px 520px,0 520px)}
.orange-edge{left:0;top:428px;width:683px;height:160px;background:var(--orange);clip-path:polygon(0 144px,683px 4px,683px 14px,0 154px)}
.seal-right{left:472px;top:393px;width:156px;height:156px;border-radius:50%;background:var(--white);border:7px solid var(--blue);display:flex;align-items:center;justify-content:center;text-align:center;font-weight:700;font-size:14px;color:var(--blue);padding:16px;line-height:1.25}
.benefits{left:48px;top:596px;width:605px;color:var(--white);font-size:12px;line-height:16px}
.benefits li{list-style:none;position:relative;padding-left:16px;margin-bottom:10px}
.benefits li::before{content:"✓";position:absolute;left:0;top:0;color:var(--yellow);font-size:11px}
.access{left:56px;top:794px;width:470px;color:var(--yellow);font-weight:700;font-size:18px;line-height:24px}
.red-base{left:0;top:840px;width:683px;height:120px;background:var(--red);clip-path:polygon(0 10px,683px 60px,683px 120px,0 120px)}
.contacts{left:48px;top:880px;color:var(--white);font-size:12.5px;line-height:17px}
.contacts .small{font-size:9.5px;line-height:15px}
.contact-row{display:flex;align-items:center;gap:6px}
.dot{width:9px;height:9px;border-radius:50%;background:var(--white);display:inline-block}
.brand-badge{left:505px;top:790px;width:148px;height:148px;border-radius:50%;background:var(--white);border:7px solid var(--blue-dark);display:flex;align-items:center;justify-content:center;text-align:center;font-family:"Fjalla One",sans-serif;font-size:22px;line-height:1.1;color:var(--red)}
</style>
</head>
<body>

<section class="page page--tournament" aria-label="Tournament flyer">
  <div class="abs hero-photo" role="img" aria-label="Photo of a classroom with a teacher speaking to seated pupils"></div>
  <div class="abs brand-tag">Vantor Oratory</div>
  <div class="abs orange-field"></div>
  <div class="abs edge-strip"></div>
  <div class="abs ribbon"></div>
  <div class="abs ribbon-chevron"></div>
  <div class="abs seal">Brindlecombe Town Council</div>
  <p class="abs ribbon-text">Promoting debating skills for all young people, promoting debating skills for all young people</p>

  <h1 class="abs invite-banner">You are warmly invited to attend the first Brindlecombe Primary Schools Vantor Debating Tournament</h1>

  <div class="abs board-paper"></div>
  <div class="abs board-post" style="left:118px"></div>
  <div class="abs board-post" style="left:293px"></div>
  <ul class="abs board">
    <li>It all blasts off on <span class="em">21st June at 9:30am</span>, when 10 teams of Year 4s and 5s battle it out, critically discussing controversial topics with articulacy and confidence</li>
    <li>The 4 most persuasive and responsive teams will then skyrocket into the semis and finals on <span class="em">29th June from 12:30pm</span></li>
    <li>All debates are held at Ashcombe Park School, Northgate Road, Brindlecombe BR4 7QT</li>
    <li>Come and see how far and fast our Key Stage 2 pupils have travelled</li>
  </ul>

  <div class="abs blue-band"></div>
  <div class="abs kids-photo" role="img" aria-label="Photo of two smiling children raising their arms"></div>
  <div class="abs launch-copy">
    <p>We'll be launching our unique, progression-based after-school clubs for primary schools at this event.</p>
    <p>Zoom over at any time. We're committed to safeguarding our intrepid debaters, so please <span class="hot">RSVP</span> to <span class="hot">info@vantororatory.org</span> with day and time of attendance, or with any queries.</p>
  </div>
  <p class="abs support">KINDLY SUPPORTED BY BRINDLECOMBE TOWN COUNCIL AND ASHCOMBE PARK SCHOOL.</p>
  <div class="abs red-foot"></div>
  <div class="abs foot-web">
    <svg width="15" height="15" viewBox="0 0 16 16" aria-hidden="true"><g fill="none" stroke="#fff" stroke-width="1.4"><circle cx="8" cy="8" r="7"/><ellipse cx="8" cy="8" rx="3" ry="7"/><line x1="1" y1="8" x2="15" y2="8"/></g></svg>
    WWW.VANTORORATORY.ORG
  </div>
</section>

<section class="page page--clubs" aria-label="After-school clubs flyer">
  <div class="abs sun-band"></div>
  <div class="abs colour-band" role="img" aria-label="Illustration of a row of coloured pencils"></div>
  <div class="abs orange-stripe"></div>
  <div class="abs white-cut"></div>
  <h2 class="abs tagline">Promoting debating skills for all young people</h2>

  <div class="abs group-photo" role="img" aria-label="Photo of cheering primary school children with arms raised"></div>
  <svg class="abs call-arrows" width="112" height="70" viewBox="0 0 112 70" aria-hidden="true">
    <polygon points="40,0 70,0 36,35 70,70 40,70 6,35" fill="#d3141c"/>
    <polygon points="80,0 112,0 78,35 112,70 80,70 46,35" fill="#d3141c"/>
  </svg>
  <h2 class="abs call-banner">CALLING ALL PRIMARY AND PREP SCHOOLS</h2>

  <div class="abs orange-edge"></div>
  <div class="abs blue-field"></div>
  <div class="abs seal-right">Brindlecombe Town Council</div>

  <ul class="abs benefits">
    <li>Give your children the skills to speak confidently, think critically and expand their horizons. Give your teachers the chance to lead them</li>
    <li>We've devised a weekly programme to ensure debating becomes a truly enriching part of your school's culture. Clubs are progression-based and teach skills explicitly each week. They allow control of learning to be in pupils' hands, using specifically-designed debating notebooks and stickers for each child to encourage reflection, research and full participation.</li>
    <li>Our programme is fun, challenging and varied. It also upskills teachers keen to take their pupils' debating to the next level. We're always on hand to help online, or in person where possible. By the end of the year we'll ensure we visit you for a day to help you embed debating into your curriculum. You can also opt to enter your pupils for the Level 1 Debating qualification from the National Speech Board, for which they will be fully prepared.</li>
  </ul>
  <p class="abs access">We're committed to access for all, so please contact for pricing options.</p>

  <div class="abs red-base"></div>
  <div class="abs contacts">
    <div class="contact-row">
      <svg width="13" height="13" viewBox="0 0 16 16" aria-hidden="true"><g fill="none" stroke="#fff" stroke-width="1.4"><circle cx="8" cy="8" r="7"/><ellipse cx="8" cy="8" rx="3" ry="7"/><line x1="1" y1="8" x2="15" y2="8"/></g></svg>
      www.vantororatory.org.
    </div>
    <div class="contact-row small"><span class="dot"></span>VANTORORATORY@VANTORORATORY</div>
    <div class="contact-row small">
      <svg width="10" height="8" viewBox="0 0 10 8" aria-hidden="true"><rect x=".5" y=".5" width="9" height="7" fill="none" stroke="#fff"/><polyline points=".5,.5 5,4.5 9.5,.5" fill="none" stroke="#fff"/></svg>
      info@vantororatory.org
    </div>
  </div>
  <div class="abs brand-badge">Vantor<br>Oratory</div>
</section>

</body>
</html>
```